Lumen Wire Outlet - bag design for fiber optic cables

We need a packaging design for a clear ziplock bag that is 7" wide and 10" high. The design will be for a new line of fiber optic cable products. You can see the products on lumenwireoutlet.example. We would like to see designs that represent a superior quality product and an American brand. We want the equivalent of a nice retail bag that you would find in a store like Tech Haven. It should be a maximum of three colors. We really want something sharp, professional and eye catching, not whimsical or cartoonish. I've included a couple of examples below. I don't really like the designs attached but it will give you an idea. Please keep in mind the bag will be clear, not white.

Target Market(s)

Men 25-65

Industry/Entity Type

Optic

Colors

Designer to choose colors to be used in the design.

Requirements
Must have
• A clean design, not overly cluttered. These cables will be selling internationally so we need to show off the fact that we're an American brand. With that said, I don't want red, white and blue and over- the- top American. I would like something more subtle, classy that still says we are a USA brand. The bag should also incorporate the logo, which is attached. Please make it 3 colors maximum.
Nice to have
• clean, professional. The design doesn't need to have the colors in the logo. I'm open to any new colors introduced.
Should not have
• whimsical, colorful

```html
<!DOCTYPE html>
<html lang="en">
<head>
<meta charset="utf-8">
<title>Lumen Wire Outlet – Fibre Optic Cable Bag</title>
<link href="https://fonts.googleapis.com/css2?family=Roboto:wght@400;700&family=Fira+Sans:wght@700&display=swap" rel="stylesheet">
<style>
  :root {
    --backdrop: #333132;
    --bag-light: #ffffff;
    --bag-silver: #d9d9d9;
    --bag-edge: #9a9a9a;
    --brand-maroon: #7c1434;
    --teal-deep: #138a80;
    --teal-light: #7fc9c6;
    --text-grey: #8c8c8c;
    --band-dark: #555555;
    --ink: #2b2b2b;
  }
  html, body {
    margin: 0;
    width: 1200px;
    height: 1200px;
    overflow: hidden;
    background: var(--backdrop);
  }
  .bag {
    position: absolute;
    left: 210px;
    top: 100px;
    width: 780px;
    height: 1000px;
    border-radius: 40px;
    overflow: hidden;
    background:
      linear-gradient(90deg, rgba(200,200,200,.7) 0%, rgba(255,255,255,0) 18%, rgba(255,255,255,0) 80%, rgba(190,190,190,.8) 100%),
      linear-gradient(180deg, var(--bag-silver) 0%, var(--bag-light) 12%, #f2f2f2 18%, #cfcfcf 19.5%, var(--bag-light) 30%, var(--bag-light) 100%);
    box-shadow: 0 0 0 2px var(--bag-edge);
  }
  .dot-texture {
    position: absolute;
    left: 0;
    top: 0;
    width: 560px;
    height: 560px;
    background: radial-gradient(ellipse at 30% 35%, rgba(170,170,170,.28) 0%, rgba(200,200,200,.12) 45%, rgba(255,255,255,0) 70%);
  }
  .dot-texture-lower {
    left: 360px;
    top: 560px;
    width: 320px;
    height: 340px;
    background: radial-gradient(ellipse at 60% 50%, rgba(170,170,170,.22) 0%, rgba(255,255,255,0) 70%);
  }
  .hang-hole {
    position: absolute;
    left: 300px;
    top: 52px;
    width: 200px;
    height: 56px;
    border-radius: 28px;
    background: var(--backdrop);
  }
  .hang-hole::before {
    content: "";
    position: absolute;
    left: 74px;
    top: -22px;
    width: 44px;
    height: 44px;
    border-radius: 50%;
    background: var(--backdrop);
  }
  .seal-line {
    position: absolute;
    left: 0; right: 0;
    top: 178px;
    height: 3px;
    background: #8e8e8e;
  }
  .cable-artwork {
    position: absolute;
    inset: 0;
  }
  .brand {
    position: absolute;
    left: 72px;
    top: 242px;
    display: flex;
    align-items: center;
    gap: 14px;
    font-family: "Roboto", sans-serif;
    font-weight: 700;
    font-size: 38px;
    letter-spacing: -0.5px;
    color: var(--brand-maroon);
  }
  .brand-mark {
    width: 26px;
    height: 26px;
    border-radius: 50%;
    background: var(--brand-maroon);
  }
  .product-name {
    position: absolute;
    left: 90px;
    top: 455px;
    margin: 0;
    font-family: "Roboto", sans-serif;
    font-weight: 700;
    font-size: 19px;
    line-height: 24px;
    color: var(--text-grey);
  }
  .category-band {
    position: absolute;
    left: 0; right: 0;
    top: 890px;
    height: 40px;
    background: linear-gradient(90deg, var(--band-dark) 0%, #bdbdbd 40%, #e0e0e0 60%, #9a9a9a 100%);
    display: flex;
    align-items: center;
    justify-content: center;
    padding-left: 120px;
    box-sizing: border-box;
    font-family: "Fira Sans", sans-serif;
    font-weight: 700;
    font-size: 27px;
    letter-spacing: 2px;
    color: var(--ink);
  }
  .origin {
    position: absolute;
    left: 0; right: 0;
    top: 944px;
    padding-left: 120px;
    text-align: center;
    font-family: "Fira Sans", sans-serif;
    font-weight: 700;
    font-size: 17px;
    letter-spacing: 3px;
    color: #5a5a5a;
  }
</style>
</head>
<body>
  <div class="bag">
    <div class="dot-texture" role="img" aria-label="Soft grey halftone dot texture"></div>
    <div class="dot-texture dot-texture-lower" role="img" aria-label="Soft grey halftone dot texture"></div>
    <svg class="cable-artwork" viewBox="0 0 780 1000" width="780" height="1000" role="img" aria-label="Flowing fibre optic cable strands in teal and maroon">
      <defs>
        <linearGradient id="cable-tones" x1="0" y1="0" x2="1" y2="0">
          <stop offset="0" stop-color="#bfe3e1"/>
          <stop offset=".35" stop-color="var(--teal-light)"/>
          <stop offset=".6" stop-color="var(--teal-deep)"/>
          <stop offset=".8" stop-color="#5e6f74"/>
          <stop offset="1" stop-color="var(--brand-maroon)" stop-opacity=".55"/>
        </linearGradient>
      </defs>
      <path d="M600 0 L780 0 L780 1000 L570 1000 C600 760 700 520 660 300 C640 180 620 90 600 0 Z" fill="url(#cable-tones)" opacity=".85"/>
    </svg>
    <div class="hang-hole"></div>
    <div class="seal-line"></div>
    <div class="brand"><span class="brand-mark"></span>Lumen Wire Outlet</div>
    <p class="product-name">Om1 LC LC Duplex Fiber Patch<br>Cable 62.5/125 Multimode</p>
    <div class="category-band">FIBRE OPTIC CABLE</div>
    <div class="origin">MADE IN USA</div>
  </div>
</body>
</html>
```